Global Expert Network Firm needs business card design

We need business card design for a new company based in Seoul, South Korea called 'Corwell Insight Partners'. We recruit industry experts covering all countries and connect our client and recruited expert by phone, face-to-face meetings and etc. We are a global expert network firm that is focused on delivering high-quality experts to our clients throughout the world. Our clients include multinational corporations, global consulting firms, private equity firms, venture capital firms, asset management companies.
We have made new logo and please find attachment.(Please use new logo)
Target Market(s)
Global Consulting Firms, Investment Firms, Private Equity Firms, Venture Capital Firms.
Industry/Entity Type
Recruitment
Contact Information for Business Card
We need two Languages (English and Korean Version).
The front is Korean and the back is English version.
[The back] [English]
Company Name: Corwell Insight Partners, Inc.
CEO Name: Daniel Park
Address: #507, Hanbit Bldg, 82 Maebongsan-ro, Dobong-gu, Seoul, 01327, Korea
Tel. +82 2 718 4052
Fax. +82 2 864 1097
Mobile. +82 10 7264 8815
Email: daniel@corwellip.com
Web: www.corwellip.com
[The front] [Korean] => Described in same order as English version.
회사명: 코웰인사이트파트너스(주)
대표이사: 박도현
주소: 서울시 도봉구 매봉산로 82 한빛빌딩 507호
Tel. 02 718 4052
Fax. 02 864 1097
Mobile. 010 7264 8815
Web: www.corwellip.com
Look and feel
Each slider illustrates characteristics of the customer's brand and the style your logo design should communicate.

```html
<!DOCTYPE html>
<html lang="en">
<head>
<meta charset="utf-8">
<title>Corwell Insight Partners – Business Card (English)</title>
<link rel="stylesheet" href="https://fonts.googleapis.com/css2?family=Source+Sans+3:wght@400&display=swap">
<style>
  :root {
    --navy: #1b2350;
    --white: #ffffff;
    --accent-red: #d2412a;
    --accent-orange: #f15a24;
    --accent-rust: #9e3312;
  }
  html, body {
    margin: 0;
    padding: 0;
    overflow: hidden;
  }
  .card-back {
    position: relative;
    width: 1200px;
    height: 667px;
    background: var(--navy);
    overflow: hidden;
    font-family: "Source Sans 3", "Myriad Pro", Arial, sans-serif;
  }
  .contact-block {
    position: absolute;
    left: 139px;
    top: 196px;
    height: 263px;
    border-left: 6px solid var(--white);
    padding-left: 19px;
    box-sizing: border-box;
  }
  .contact-list {
    margin: 0;
    padding: 0;
    list-style: none;
    color: var(--white);
    font-size: 22.5px;
    line-height: 28.2px;
    letter-spacing: 0.3px;
  }
  .corner-accent {
    position: absolute;
    left: 0;
    bottom: 0;
    width: 280px;
    height: 265px;
  }
</style>
</head>
<body>
  <main class="card-back">
    <section class="contact-block" aria-label="Company contact details">
      <ul class="contact-list">
        <li>Company Name : Corwell Insight Partners, Inc.</li>
        <li>CEO Name : Daniel Park</li>
        <li>Address : #507, Hanbit Bldg, 82 Maebongsan-ro, Dobong-gu,</li>
        <li>Seoul, 01327, Korea</li>
        <li>Tel. +82 2 718 4052</li>
        <li>Fax. +82 2 864 1097</li>
        <li>Mobile. +82 10 7264 8815</li>
        <li>Email : daniel@corwellip.com</li>
        <li>Web : www.corwellip.com</li>
      </ul>
    </section>

    <svg class="corner-accent" viewBox="0 402 280 265" role="img" aria-label="Warm red-orange geometric corner decoration">
      <defs>
        <linearGradient id="corner-warmth" x1="0" y1="0" x2="1" y2="1">
          <stop offset="0" stop-color="var(--accent-red)"/>
          <stop offset="0.55" stop-color="var(--accent-orange)"/>
          <stop offset="1" stop-color="var(--accent-rust)"/>
        </linearGradient>
      </defs>
      <polygon points="0,404 277,667 0,667" fill="url(#corner-warmth)"/>
    </svg>
  </main>
</body>
</html>
```